ROLL-UP DESIGN FOR SUPERMARKET DELIVERY

We need the graphic design of a roll-up with measurements 200 cm height x cm 85 width, for a supermarket delivery service.

The main logo "The Velarno" either color version or black version must be present very visible on the design.

the second logo attached 'CALVESINOSHOP' must also be present but smaller on the design.

the following text must be present on the design: CONSEGNA STESSO GIORNO.

Printing instruction attached must be respected.

Target Market(s)

HIGH END ITALIAN AND EUROPEAN SUPERMARKET CLIENTELE

Industry/Entity Type

FOOD DELIVERY

Requirements
Must have
• LOGOS ATTACHED
Nice to have
• PHOTOS OF SEA, SARDINIA, LUXURY DELIVERY, YACHTS

```html
<!DOCTYPE html>
<html lang="it">
<head>
<meta charset="utf-8">
<title>The Velarno – Consegna stesso giorno</title>
<link rel="stylesheet" href="https://fonts.googleapis.com/css2?family=Montserrat:wght@600;700;800&display=swap">
<style>
  :root {
    --sun: #fbbf45;
    --white: #ffffff;
    --sea-light: #8a8a1c;
    --sea-mid: #4f6b1f;
    --sea-deep: #0f2a10;
    --base-grey: #939598;
    --brand-ink: #c0561f;
    --ink-dark: #333333;
  }
  html, body { margin: 0; padding: 0; overflow: hidden; }
  body { width: 1200px; height: 3102px; background: var(--white); font-family: "Montserrat", sans-serif; }
  .rollup { position: relative; width: 1200px; height: 3102px; overflow: hidden; }
  .hero-photo {
    position: absolute; left: 4px; top: 4px; width: 1192px; height: 2808px;
    background: linear-gradient(100deg, var(--sea-light) 0%, #7c7f1a 35%, var(--sea-mid) 55%, #2f5a1c 75%, var(--sea-deep) 100%);
  }
  .base-band { position: absolute; left: 0; top: 2820px; width: 1200px; height: 282px; background: var(--base-grey); }
  .brand { position: absolute; left: 380px; top: 74px; width: 680px; text-align: center; }
  .brand-name {
    margin: 0; color: var(--sun); font-weight: 800; font-size: 96px;
    letter-spacing: -3px; line-height: 1; white-space: nowrap;
  }
  .brand-tagline {
    margin: 28px 0 0; color: var(--white); font-weight: 700; font-size: 40px;
    letter-spacing: 9px; line-height: 1; white-space: nowrap;
  }
  .graphics { position: absolute; left: 0; top: 0; }
  .headline { font-family: "Montserrat", sans-serif; font-weight: 800; fill: var(--sun); }
  .partner {
    position: absolute; left: 398px; top: 2665px; width: 370px; height: 80px;
    background: var(--white); text-align: center; box-sizing: border-box; padding-top: 10px;
  }
  .partner-name { display: block; color: var(--brand-ink); font-weight: 800; font-size: 34px; line-height: 1; letter-spacing: 1px; }
  .partner-tagline { display: block; color: var(--ink-dark); font-weight: 600; font-size: 17px; margin-top: 8px; white-space: nowrap; }
</style>
</head>
<body>
<main class="rollup">
  <div class="hero-photo" role="img" aria-label="Photo of a yacht deck with a coiled mooring rope by the rail over the sea, toned in olive and green"></div>
  <div class="base-band"></div>

  <header class="brand">
    <h1 class="brand-name">The Velarno</h1>
    <p class="brand-tagline">ORDINA TUTTO</p>
  </header>

  <svg class="graphics" width="1200" height="3102" viewBox="0 0 1200 3102">
    <g class="spikes">
      <polygon points="534,401 510,925 558,925" fill="var(--sun)"/>
      <polygon points="682,401 658,925 706,925" fill="var(--white)"/>
      <polygon points="830,401 806,925 854,925" fill="var(--sun)"/>
      <polygon points="978,401 954,925 1002,925" fill="var(--white)"/>
    </g>
    <text class="headline" transform="translate(355 2392) rotate(-90)" font-size="325" textLength="1946" lengthAdjust="spacingAndGlyphs">CONSEGNA</text>
    <text class="headline" transform="translate(697 2398) rotate(-90)" font-size="325" textLength="1374" lengthAdjust="spacingAndGlyphs">STESSO</text>
    <text class="headline" transform="translate(1034 2392) rotate(-90)" font-size="325" textLength="1370" lengthAdjust="spacingAndGlyphs">GIORNO</text>
  </svg>

  <div class="partner">
    <span class="partner-name">CALVESINOSHOP</span>
    <span class="partner-tagline">La spesa fresca ogni giorno</span>
  </div>
</main>
</body>
</html>
```